Business cards - ZELTO Roofing & Siding

We need simple business cards made up for our Roofing & Siding business based in Calgary Alberta.
The logo on one side of the card and potentially our slogan "Built with care, proven over years".
The other side could have:
-A small logo
-Rep name:
-Rep cell phone:
-Rep email:
-Office phone: 403-688-2904
-Website: PrairieTopCrafters.com

We would like to incorporate the colours from our logo, especially the lite blue on the jpeg file. I have attached the ai file and jpeg file. We like the colours better on the jpeg file.

```html
<!DOCTYPE html>
<html lang="en">
<head>
<meta charset="utf-8">
<title>ZELTO Roofing &amp; Siding — Business Cards</title>
<link href="https://fonts.googleapis.com/css2?family=Roboto:wght@400;500&display=swap" rel="stylesheet">
<style>
  :root {
    --backdrop: #e9e9ec;
    --card: #ffffff;
    --brand-blue: #3f7fc4;
    --ink: #111111;
    --mark-ink: #262626;
    --slogan-grey: #7a7a7a;
    --title-navy: #1d3a7a;
    --icon-grey: #a6a6a6;
  }
  * { margin: 0; padding: 0; box-sizing: border-box; }
  html, body {
    width: 991px; height: 1200px; overflow: hidden;
    background: var(--backdrop);
    font-family: "Roboto", Arial, sans-serif;
  }
  .canvas { position: relative; width: 991px; height: 1200px; }
  .card {
    position: absolute; left: 128px; width: 735px; height: 420px;
    background: var(--card); overflow: hidden;
  }
  .card--front { top: 113px; }
  .card--back { top: 677px; }
  .card__band {
    position: absolute; left: 0; right: 0; bottom: 0; height: 12px;
    background: var(--brand-blue);
  }

  /* Wordmark */
  .wordmark {
    position: absolute; text-align: center; color: var(--mark-ink);
    font-weight: 500; transform: translateX(-50%); white-space: nowrap;
  }
  .wordmark__square { display: block; margin: 0 auto; background: var(--brand-blue); }
  .wordmark__name { display: block; line-height: 1; }
  .wordmark__sub { display: block; line-height: 1; }

  .card--front .wordmark { left: 367px; top: 168px; }
  .card--front .wordmark__square { width: 18px; height: 18px; margin-bottom: 14px; }
  .card--front .wordmark__name { font-size: 68px; letter-spacing: 10px; padding-left: 10px; }
  .card--front .wordmark__sub { font-size: 25px; letter-spacing: 6px; padding-left: 6px; margin-top: 8px; }

  .slogan {
    position: absolute; left: 0; right: 0; top: 305px; text-align: center;
    font-size: 11px; letter-spacing: 2.6px; color: var(--slogan-grey);
    text-transform: uppercase;
  }

  .card--back .wordmark { left: 545px; top: 172px; }
  .card--back .wordmark__square { width: 10px; height: 10px; margin-bottom: 10px; }
  .card--back .wordmark__name { font-size: 40px; letter-spacing: 6px; padding-left: 6px; }
  .card--back .wordmark__sub { font-size: 16px; letter-spacing: 3.5px; padding-left: 3.5px; margin-top: 6px; }

  /* Rep details */
  .rep { position: absolute; left: 57px; top: 92px; }
  .rep__name { font-size: 28px; font-weight: 500; color: var(--ink); line-height: 1.1; }
  .rep__title { font-size: 14px; color: var(--title-navy); margin-top: 2px; }

  .contacts { position: absolute; left: 57px; top: 174px; list-style: none; }
  .contact {
    display: flex; align-items: center; gap: 20px; margin-bottom: 14px;
    font-size: 14px; color: var(--ink); line-height: 16px;
  }
  .contact__icon { width: 28px; height: 28px; flex: none; }
</style>
</head>
<body>
<main class="canvas">

  <section class="card card--front" aria-label="Card front">
    <div class="wordmark">
      <span class="wordmark__square"></span>
      <span class="wordmark__name">ZELTO</span>
      <span class="wordmark__sub">ROOFING &amp; SIDING</span>
    </div>
    <p class="slogan">Built with care, proven over years</p>
    <div class="card__band"></div>
  </section>

  <section class="card card--back" aria-label="Card back">
    <div class="rep">
      <h1 class="rep__name">Your Name</h1>
      <p class="rep__title">Project Manager</p>
    </div>

    <ul class="contacts">
      <li class="contact">
        <svg class="contact__icon" viewBox="0 0 28 28" aria-hidden="true">
          <circle cx="14" cy="14" r="14" fill="var(--icon-grey)"/>
          <path d="M9 7.5c1-.6 1.8-.3 2.3.6l1.2 2.3c.4.8.2 1.5-.5 2l-.8.6c.7 1.7 1.9 3 3.6 3.8l.6-.8c.5-.7 1.2-.9 2-.5l2.3 1.2c.9.5 1.1 1.3.5 2.2-1 1.6-2.6 2-4.3 1.3-3.7-1.5-6.3-4.2-7.7-7.9-.6-1.7-.2-3.3 1.8-4.8z" fill="#fff"/>
        </svg>
        <span>+00 1234 567 8900<br>403-688-2904</span>
      </li>
      <li class="contact">
        <svg class="contact__icon" viewBox="0 0 28 28" aria-hidden="true">
          <circle cx="14" cy="14" r="14" fill="var(--icon-grey)"/>
          <rect x="6.5" y="9" width="15" height="10" fill="none" stroke="#fff" stroke-width="1.2"/>
          <path d="M6.5 9l7.5 6 7.5-6M6.5 19l5.5-5M21.5 19l-5.5-5" fill="none" stroke="#fff" stroke-width="1.2"/>
        </svg>
        <span>yourmailadress@domain.com<br>secondmail@domain.com</span>
      </li>
      <li class="contact">
        <svg class="contact__icon" viewBox="0 0 28 28" aria-hidden="true">
          <circle cx="14" cy="14" r="14" fill="var(--icon-grey)"/>
          <g fill="none" stroke="#fff" stroke-width="1.1">
            <circle cx="14" cy="14" r="8"/>
            <ellipse cx="14" cy="14" rx="3.6" ry="8"/>
            <path d="M6 14h16M7.2 10h13.6M7.2 18h13.6M14 6v16"/>
          </g>
        </svg>
        <span>PrairieTopCrafters.com</span>
      </li>
    </ul>

    <div class="wordmark">
      <span class="wordmark__square"></span>
      <span class="wordmark__name">ZELTO</span>
      <span class="wordmark__sub">ROOFING &amp; SIDING</span>
    </div>
    <div class="card__band"></div>
  </section>

</main>
</body>
</html>
```